Need simple and modern looking business card with all my information on one side and logo on the other side
Info :
Company name - VELMAR CONSTRUCTION LLC
Company addres- 418 harbor 87th. Dunmoor park ny 10352
Email- velmarllc@tridomail.Com
Company phone number 555-318-6094
Cell number- 555-742-0583
Web site - velmarllc.Com
My name Gerald tomasino

Target Market(s)

Construction , home improvement, remodeling

Industry/Entity Type

Construction

Contact Information for Business Card

It has to be moder but at the same time simple

Font styles to use
Sans Serif

Colors
0255a3
ffffff
000000
f78f20
b1b1b1
9d9d9d
1b1b1b
33a6d7
ec1f27

Requirements
Must have
• My logo on one side maybe with a some kind of background on the other side all my information
Nice to have
• Some kind of background pictures provided by you .PLEASE HAVE ACCOUNT WITH PIXELVAULT WILL NOT PAY ANY EXTRA FEES .
Should not have
• Any kind of hamer, nails,screws, helmets itp. Please do not copy the other designs come up with something new.

```html
<!DOCTYPE html>
<html lang="en">
<head>
<meta charset="utf-8">
<title>Velmar Construction LLC – Business Card</title>
<link href="https://fonts.googleapis.com/css2?family=Montserrat:wght@400;600;700&family=Roboto+Condensed:wght@400;700&display=swap" rel="stylesheet">
<style>
  :root {
    --blue: #0255a3;
    --white: #ffffff;
    --black: #000000;
    --orange: #f78f20;
    --grey-light: #b1b1b1;
    --grey: #9d9d9d;
    --ink: #1b1b1b;
    --sky: #33a6d7;
    --red: #ec1f27;
    --backdrop: #eceded;
  }
  * { margin: 0; padding: 0; box-sizing: border-box; }
  html, body { width: 1200px; height: 893px; overflow: hidden; }
  body {
    background: var(--backdrop);
    font-family: "Roboto Condensed", Arial, sans-serif;
    position: relative;
  }
  .card {
    position: absolute;
    top: 296px;
    width: 525px;
    height: 300px;
    box-shadow: 0 6px 18px rgba(0,0,0,.18);
  }
  .card--front { left: 50px; background: var(--white); }
  .card--back  { left: 625px; background: var(--black); overflow: hidden; }

  .brand {
    position: absolute;
    display: flex;
    align-items: center;
    gap: 10px;
    font-family: "Montserrat", Arial, sans-serif;
    font-weight: 600;
    color: var(--ink);
    line-height: 1;
  }
  .brand__mark { width: 14px; height: 14px; background: var(--orange); }
  .brand__name { font-size: 30px; letter-spacing: 1px; }
  .brand__sub  { font-size: 11px; letter-spacing: 2.6px; margin-top: 5px; display: block; }
  .card--front .brand { top: 52px; right: 38px; }
  .card--back .brand { top: 112px; right: 34px; color: var(--white); }
  .card--back .brand__mark { background: var(--white); }

  .person { position: absolute; left: 38px; top: 150px; }
  .person__name {
    color: var(--blue);
    font-weight: 700;
    font-size: 17px;
    letter-spacing: .5px;
    text-transform: uppercase;
  }
  .person__title { color: var(--grey); font-size: 12px; margin-top: 2px; }

  .contact {
    position: absolute;
    left: 38px;
    right: 38px;
    top: 210px;
    color: var(--ink);
    font-size: 12px;
    line-height: 1.7;
  }
  .contact__sep { color: var(--grey-light); padding: 0 6px; }
  .contact__web { position: absolute; right: 0; bottom: 0; color: var(--ink); }

  .backdrop-photo {
    position: absolute;
    left: 40px;
    top: 30px;
    width: 260px;
    height: 240px;
    background: radial-gradient(ellipse at 50% 55%, #2b3038 0%, #15181d 50%, var(--black) 80%);
  }
</style>
</head>
<body>
  <section class="card card--front" aria-label="Business card, information side">
    <div class="brand">
      <span class="brand__mark"></span>
      <div>
        <span class="brand__name">VELMAR</span>
        <span class="brand__sub">CONSTRUCTION LLC</span>
      </div>
    </div>
    <div class="person">
      <p class="person__name">Gerald Tomasino</p>
      <p class="person__title">President</p>
    </div>
    <div class="contact">
      <p>C: 555-742-0583<span class="contact__sep">|</span>P: 555-318-6094<span class="contact__sep">|</span>velmarllc@tridomail.com</p>
      <p>418 Harbor 87th. Dunmoor Park NY 10352</p>
      <p class="contact__web">www.velmarllc.com</p>
    </div>
  </section>

  <section class="card card--back" aria-label="Business card, logo side">
    <div class="backdrop-photo" role="img" aria-label="Dark night photograph of a city skyline"></div>
    <div class="brand">
      <span class="brand__mark"></span>
      <div>
        <span class="brand__name">VELMAR</span>
        <span class="brand__sub">CONSTRUCTION LLC</span>
      </div>
    </div>
  </section>
</body>
</html>
```